Direct Mail Postcard- Lighting Company

Our task is to send a postcard directly to houses surrounding where our company has done work. My goal is to position ourselves as the go to outdoor lighting partner for their neighborhood.
Trusted Lighting Design & Maintenance Your neighbor chose us to enhance and maintain their home's beauty and security. Now, we're offering our top-tier services to the entire neighborhood.
Please emphasize our:
Maintenance Excellence:
Regular system check-ups
Prompt repair and replacement
Upgrades to the latest technology
Less emphasis on:
Our Services:
High-Quality Landscape & Architectural Lighting
Reliable Permanent Lighting Solutions
Call us today and take advantage of our 25% discount (limited time offer)
For more details or to schedule a consultation, visit glowcrest-mo.com or call .
*Need to be able to tweak this for future campaigns. Quickly edit verbiage for future marketing campaigns. I.e. a file that can be edited through Canva
*Inspiration photo file (Yard Beacon Concepts)
*Would like to incorporate the before and after png
Call: (816) 555-0193
glowcrest-mo.com
Updates
I attached a new before and after photo. Please create a design implementing this
Look and feel
Each slider illustrates characteristics of the customer's brand and the style your logo design should communicate.

```html
<!DOCTYPE html>
<html lang="en">
<head>
<meta charset="utf-8">
<title>Glowcrest Lighting – Neighborhood Postcard</title>
<link rel="stylesheet" href="https://fonts.googleapis.com/css2?family=Oswald:wght@200;400;600;700&family=Josefin+Sans:wght@300&family=Arimo:wght@400;700&display=swap">
<style>
:root{
  --page:#2a2d3e;
  --ink:#0f0d0b;
  --band:#15120f;
  --gold:#d9a84a;
  --amber:#f2a93b;
  --orange:#ef8a1f;
  --headline-grey:#dcd6ca;
  --green:#a6cf2f;
  --cream:#ecd591;
  --lavender:#8587a8;
  --call-yellow:#f3c25a;
  --white:#ffffff;
  --muted:#bfb8ad;
}
*{box-sizing:border-box;margin:0;padding:0}
html,body{width:1200px;height:2910px;overflow:hidden}
body{background:var(--page);font-family:"Arimo",Arial,sans-serif;position:relative}
.postcard{position:absolute;left:170px;width:860px;height:1220px;overflow:hidden;background:var(--ink);box-shadow:0 20px 40px rgba(0,0,0,.45)}
.postcard--front{top:120px}
.postcard--back{top:1570px}
.night-photo{position:absolute;left:0;top:0;width:860px;height:1005px;
  background:
   radial-gradient(ellipse 260px 180px at 450px 820px,rgba(224,150,60,.55),transparent 70%),
   radial-gradient(ellipse 300px 200px at 700px 250px,rgba(70,80,130,.6),transparent 70%),
   linear-gradient(180deg,#3a4170 0%,#2b2f4a 35%,#2a2520 70%,#181410 100%)}
.bottom-band{position:absolute;left:0;top:1005px;width:860px;height:215px;background:var(--band)}
.brand-box{position:absolute;left:40px;top:0;width:300px;height:130px;background:#0b0a09;display:flex;flex-direction:column;justify-content:center;align-items:center}
.brand-name{font-family:"Josefin Sans",sans-serif;font-weight:300;color:var(--white);line-height:1;text-align:center}
.brand-name .top{display:block;font-size:40px;letter-spacing:5px}
.brand-name .bottom{display:block;font-size:24px;letter-spacing:15px;margin-top:8px}
.headline{position:absolute;left:455px;top:40px;width:370px;font-family:"Oswald",sans-serif;font-weight:700;line-height:1.08;text-transform:uppercase}
.headline .l1{color:var(--amber);font-size:35px}
.headline .l2{color:var(--headline-grey);font-size:33px}
.headline .l3{color:var(--orange);font-size:45px}
.headline .l4{color:var(--white);font-size:23px;font-weight:600;padding-bottom:6px;border-bottom:3px solid var(--gold)}
.headline-note{position:absolute;left:455px;top:250px;width:370px;color:var(--muted);font-family:"Oswald",sans-serif;font-weight:200;font-size:12.5px;line-height:1.45;text-align:center;text-transform:uppercase}
.headline-note p+p{margin-top:10px}
.compare{position:absolute;left:0;top:0;width:860px;height:860px}
.service-box{position:absolute;top:880px;width:330px;height:96px;border:1.5px solid #cfc8bc;border-radius:8px;background:rgba(0,0,0,.35);color:var(--white);font-size:15px;line-height:1.3;text-align:center;padding-top:22px}
.service-box--maintenance{left:80px}
.service-box--services{left:460px}
.service-box .tag{position:absolute;left:30px;right:30px;top:-11px;background:var(--orange);color:var(--white);font-size:15px;line-height:20px;text-transform:uppercase}
.call-tag{position:absolute;left:175px;top:1040px;width:520px;height:70px;transform:rotate(-8deg);background:var(--lavender);clip-path:polygon(4% 0,100% 0,96% 100%,0 100%);color:var(--white);font-weight:700;font-size:40px;line-height:70px;text-align:center}
.site-url{position:absolute;left:0;width:860px;text-align:center;color:var(--orange);font-size:22px}
.postcard--front .site-url{top:1165px}
.glow-column{position:absolute;left:250px;top:0;width:360px;height:1005px;background:rgba(190,110,40,.32)}
.back-headline{position:absolute;left:250px;top:36px;width:360px;text-align:center;font-family:"Oswald",sans-serif;text-transform:uppercase;line-height:1.05}
.back-headline .magic{color:var(--green);font-weight:700;font-size:58px}
.back-headline .night{color:var(--white);font-weight:200;font-size:56px}
.back-headline .glow{display:inline-block;margin-top:4px;background:var(--cream);color:#1c1a16;font-family:"Arimo",sans-serif;font-size:30px;padding:0 10px;line-height:38px}
.back-brand{position:absolute;left:250px;top:230px;width:360px}
.gallery{position:absolute;left:0;top:0;width:860px;height:1005px}
.arrow{position:absolute;left:405px;width:0;height:0;border-left:25px solid transparent;border-right:25px solid transparent}
.arrow--up{top:1020px;border-bottom:22px solid var(--gold)}
.arrow--down{top:1125px;border-top:22px solid var(--gold)}
.back-call{position:absolute;left:0;top:1052px;width:860px;text-align:center;color:var(--call-yellow);font-weight:700;font-size:40px}
.url-box{position:absolute;left:250px;top:1152px;width:360px;height:68px;background:#201b16}
.postcard--back .site-url{top:1172px}
</style>
</head>
<body>

<section class="postcard postcard--front" aria-label="Postcard front">
  <div class="night-photo" role="img" aria-label="Softly blurred photo of a home lit at dusk"></div>
  <div class="bottom-band"></div>

  <div class="brand-box">
    <div class="brand-name"><span class="top">GLOWCREST</span><span class="bottom">LIGHTING</span></div>
  </div>

  <h1 class="headline">
    <div class="l1">Elevate your outdoor</div>
    <div class="l2">spaces with premium</div>
    <div class="l3">lighting trusted</div>
    <div class="l4">Lighting design &amp; maintenance</div>
  </h1>
  <div class="headline-note">
    <p>Your neighbor chose us to enhance and maintain<br>their home's beauty and security.</p>
    <p>Now, we're offering our top-tier services<br>to the entire neighborhood.</p>
  </div>

  <svg class="compare" viewBox="0 0 860 860" width="860" height="860">
    <defs>
      <radialGradient id="beforeFill" cx="50%" cy="45%" r="60%">
        <stop offset="0" stop-color="#262a35"/><stop offset="1" stop-color="#07080b"/>
      </radialGradient>
      <radialGradient id="afterFill" cx="50%" cy="45%" r="60%">
        <stop offset="0" stop-color="#c9bda6"/><stop offset=".55" stop-color="#5d5a55"/><stop offset="1" stop-color="#14161c"/>
      </radialGradient>
      <path id="beforeArc" d="M 10 500 A 205 205 0 0 0 250 655"/>
      <path id="afterArc" d="M 470 515 A 205 205 0 0 1 810 515"/>
    </defs>
    <circle cx="210" cy="455" r="185" fill="url(#beforeFill)" stroke="var(--gold)" stroke-width="6" role="img" aria-label="Before photo: the house at night without lighting"/>
    <circle cx="640" cy="630" r="185" fill="url(#afterFill)" stroke="var(--gold)" stroke-width="6" role="img" aria-label="After photo: the same house with landscape lighting"/>
    <text font-family="Josefin Sans, sans-serif" font-size="34" fill="#e8e2d6" letter-spacing="5" text-anchor="middle"><textPath href="#beforeArc" startOffset="50%">BEFORE</textPath></text>
    <text font-family="Josefin Sans, sans-serif" font-size="34" fill="#e8e2d6" letter-spacing="5" text-anchor="middle"><textPath href="#afterArc" startOffset="50%">AFTER</textPath></text>
    <g class="discount-badge">
      <circle cx="415" cy="595" r="86" fill="#ffffff" stroke="var(--green)" stroke-width="16"/>
      <text x="418" y="563" text-anchor="middle" font-family="Arimo, sans-serif" font-size="20" fill="#111">DISCOUNT</text>
      <text x="420" y="612" text-anchor="middle" font-family="Oswald, sans-serif" font-weight="600" font-size="50" fill="#111">25%</text>
      <text x="416" y="640" text-anchor="middle" font-family="Arimo, sans-serif" font-size="13" fill="#111">Limited Time Offer!</text>
      <g class="plug-icon" fill="var(--green)">
        <rect x="296" y="560" width="15" height="8" rx="2"/>
        <rect x="254" y="546" width="42" height="34" rx="7"/>
        <rect x="261" y="528" width="7" height="20"/>
        <rect x="282" y="528" width="7" height="20"/>
        <rect x="271" y="578" width="8" height="18"/>
      </g>
    </g>
  </svg>

  <div class="service-box service-box--maintenance">
    <div class="tag">Maintenance Excellence</div>
    Regular system check-ups<br>Prompt repair and replacement<br>Upgrades to the latest technology
  </div>
  <div class="service-box service-box--services">
    <div class="tag">Our Services</div>
    High-Quality Landscape &amp;<br>Architectural Lighting<br>Reliable Permanent Lighting Solutions
  </div>

  <div class="call-tag">Call (816) 555-0193</div>
  <div class="site-url">www.glowcrest-mo.com</div>
</section>

<section class="postcard postcard--back" aria-label="Postcard back">
  <div class="night-photo" role="img" aria-label="Softly blurred photo of a lit garden at dusk"></div>
  <div class="glow-column"></div>
  <div class="bottom-band"></div>

  <h2 class="back-headline">
    <div class="magic">Create magic</div>
    <div class="night">At night with</div>
    <div class="glow">The perfect glow</div>
  </h2>
  <div class="back-brand brand-name"><span class="top">GLOWCREST</span><span class="bottom">LIGHTING</span></div>

  <svg class="gallery" viewBox="0 0 860 1005" width="860" height="1005">
    <defs>
      <radialGradient id="warmShot" cx="50%" cy="55%" r="60%"><stop offset="0" stop-color="#d98a3a"/><stop offset="1" stop-color="#231a12"/></radialGradient>
      <radialGradient id="duskShot" cx="50%" cy="45%" r="60%"><stop offset="0" stop-color="#c7b08a"/><stop offset=".6" stop-color="#3b4a3a"/><stop offset="1" stop-color="#1a2030"/></radialGradient>
      <radialGradient id="skyShot" cx="50%" cy="35%" r="65%"><stop offset="0" stop-color="#7a78c0"/><stop offset=".6" stop-color="#4d6a3a"/><stop offset="1" stop-color="#1a1f2a"/></radialGradient>
      <radialGradient id="colorShot" cx="50%" cy="50%" r="60%"><stop offset="0" stop-color="#d94a4a"/><stop offset=".5" stop-color="#c9b030"/><stop offset="1" stop-color="#1a1a1a"/></radialGradient>
      <radialGradient id="treeShot" cx="50%" cy="50%" r="60%"><stop offset="0" stop-color="#9aa060"/><stop offset="1" stop-color="#141812"/></radialGradient>
      <radialGradient id="greenShot" cx="50%" cy="50%" r="60%"><stop offset="0" stop-color="#7ec04a"/><stop offset="1" stop-color="#10200e"/></radialGradient>
      <radialGradient id="blueShot" cx="50%" cy="45%" r="60%"><stop offset="0" stop-color="#d8c8a0"/><stop offset=".6" stop-color="#3c4c7a"/><stop offset="1" stop-color="#141a2c"/></radialGradient>
    </defs>
    <g stroke="var(--gold)" stroke-width="3" stroke-dasharray="2 5">
      <circle cx="145" cy="455" r="87" fill="url(#warmShot)" role="img" aria-label="Lit garden cottage"/>
      <circle cx="335" cy="455" r="87" fill="url(#duskShot)" role="img" aria-label="Large home with facade lighting"/>
      <circle cx="525" cy="455" r="87" fill="url(#skyShot)" role="img" aria-label="Lawn path under dusk sky"/>
      <circle cx="715" cy="455" r="87" fill="url(#colorShot)" role="img" aria-label="Patio with colored accent lights"/>
      <circle cx="145" cy="645" r="87" fill="url(#treeShot)" role="img" aria-label="Uplit trees in a backyard"/>
      <circle cx="335" cy="645" r="87" fill="url(#warmShot)" role="img" aria-label="Fire pit seating area at night"/>
      <circle cx="525" cy="645" r="87" fill="url(#warmShot)" role="img" aria-label="Walkway lined with string lights"/>
      <circle cx="715" cy="645" r="87" fill="url(#blueShot)" role="img" aria-label="Home entrance with column lighting"/>
      <circle cx="145" cy="830" r="87" fill="url(#warmShot)" role="img" aria-label="Deck with warm lighting by water"/>
      <circle cx="335" cy="830" r="87" fill="url(#warmShot)" role="img" aria-label="Wood fence with accent lights"/>
      <circle cx="525" cy="830" r="87" fill="url(#greenShot)" role="img" aria-label="Path light among plants"/>
      <circle cx="715" cy="830" r="87" fill="url(#warmShot)" role="img" aria-label="Home exterior washed in warm light"/>
    </g>
  </svg>

  <div class="arrow arrow--up"></div>
  <div class="back-call">Call (816) 555-0193</div>
  <div class="arrow arrow--down"></div>
  <div class="url-box"></div>
  <div class="site-url">www.glowcrest-mo.com</div>
</section>

</body>
</html>
```